A Military/Intel consulting firm needs a web design.

We are a niche consulting business that specializes in assisting customers get business with the Military and Intelligence agencies.

Accelerate Growth
Accelerate Time to Market
Focused Acceleration
A GROWING TEAM OF INNOVATIVE, TENACIOUS THINKERS WHO THRIVE ON SOLVING COMPLICATED PROBLEMS.
Intelligence Based Due Diligence

Target Market(s)

Technology, engineering, Unmanned Aerial Vehicle (UAV) companies and satellite operators

Industry/Entity Type

Information Technology

Coding

Coded - Design and coding required

Number of Pages Required

3 page

Requirements
Must have
• We are consultants that identify small companies that can use our services to sell in to mainly Northern Readiness Bureau or US intelligence agency.
Nice to have
• I like the feel of this site: http://kelvoranet.com/
Should not have
• None come to mind

```html
<!DOCTYPE html>
<html lang="en">
<head>
<meta charset="utf-8">
<title>Halden Group — Intelligence Based Due Diligence</title>
<link rel="stylesheet" href="https://fonts.googleapis.com/css2?family=Oswald:wght@500&family=Raleway:wght@300;400&family=Lato:wght@400;700&display=swap">
<style>
:root{
  --black:#050607;
  --night:#0a1a2a;
  --navy:#0c2f52;
  --blue:#0e3b66;
  --blue-deep:#0a2c4e;
  --ink:#ffffff;
  --soft:#c7d3df;
  --muted:#8d9aa8;
  --line:#7f9bb8;
  --grey:#b5b5b5;
}
*{margin:0;padding:0;box-sizing:border-box}
html,body{width:1200px;height:2303px;overflow:hidden;background:var(--black)}
body{font-family:'Lato',sans-serif;color:var(--ink);position:relative}
section,header,nav,footer{position:absolute;left:0;width:1200px}
.abs{position:absolute}
p{font-size:11px;line-height:17px;color:var(--soft)}

/* hero */
.hero{top:0;height:392px;background:radial-gradient(ellipse at 50% 40%,#3a3d42 0%,#16181b 45%,#050607 80%)}
.hero-art{position:absolute;inset:0}
.brand-badge{position:absolute;left:546px;top:120px;width:128px;height:128px;border-radius:50%;background:#fff;display:flex;align-items:center;justify-content:center;font-family:'Oswald',sans-serif;font-size:17px;color:var(--blue);letter-spacing:.5px}
.tagline{position:absolute;top:256px;width:100%;text-align:center;font-family:'Oswald',sans-serif;font-weight:500;font-size:15px;letter-spacing:.3px}

/* nav */
.main-nav{top:392px;height:53px;background:var(--night)}
.nav-brand{left:262px;top:17px;font-family:'Raleway',sans-serif;font-size:14px;font-weight:400}
.nav-links{right:240px;top:21px;display:flex;gap:30px;list-style:none;font-size:9px;letter-spacing:.5px;text-transform:uppercase}

/* about */
.about{top:445px;height:287px;background:var(--blue);text-align:center}
.section-title{font-family:'Raleway',sans-serif;font-weight:300;font-size:22px;letter-spacing:1px}
.about .section-title{position:absolute;top:66px;width:100%}
.about p{position:absolute;left:400px;top:112px;width:420px;font-size:10px;line-height:15px}
.text-link{font-size:9px;color:var(--ink);padding-bottom:6px;border-bottom:1px solid var(--ink)}
.about .text-link{position:absolute;left:580px;top:200px}

/* what */
.what{top:732px;height:392px;background:linear-gradient(100deg,#5d7ea3 0%,#3e6189 40%,#243f60 70%,#1a3454 100%)}
.what-title{left:258px;top:65px;font-family:'Raleway',sans-serif;font-weight:300;font-size:24px;line-height:28px;text-transform:uppercase}
.what-lead{left:258px;top:140px;width:235px;font-size:10px;line-height:15px}
.what-more{left:258px;top:310px}
.what-side{left:518px;top:70px;width:180px;border-top:1px solid var(--ink);padding-top:14px}
.what-side h3{font-size:9px;font-weight:400;text-transform:uppercase;margin-bottom:16px}
.what-side p{font-size:10px;line-height:15px}

/* services */
.services{top:1124px;height:454px;background:var(--black)}
.services .section-title{position:absolute;left:541px;top:66px}
.services-intro{left:541px;top:113px;width:420px;padding-bottom:26px;border-bottom:1px solid #555;font-size:9px;line-height:14px}
.services-art{left:255px;top:150px;width:220px;height:250px;background:linear-gradient(160deg,#1c1a14 0%,#3b321c 50%,#15130e 100%)}
.we-serve{left:250px;top:300px;width:92px;height:92px;border-radius:50%;background:var(--grey);display:flex;align-items:center;justify-content:center;font-size:11px;color:#fff}
.service{width:190px}
.service svg{position:absolute;left:-28px;top:0}
.service h4{font-size:9px;font-weight:400;text-transform:uppercase;margin-bottom:10px;color:#ddd}
.service p{font-size:8px;line-height:13px;color:var(--muted)}

/* partners */
.partners{top:1578px;height:108px;background:var(--blue);display:flex;gap:40px;align-items:center;justify-content:center;padding-right:30px}
.partner-mark{width:86px;height:30px;border-radius:3px;background:#9fb3c9;opacity:.75}

/* testimonial */
.testimonial{top:1686px;height:299px;background:linear-gradient(180deg,#3a3b3d 0%,#222325 60%,#151617 100%);text-align:center}
.quote-mark{top:68px;width:100%;font-family:'Raleway',sans-serif;font-size:26px;color:var(--grey)}
.testimonial p{position:absolute;left:330px;top:112px;width:540px;font-size:10px;line-height:15px}
.author{top:166px;width:100%;font-size:10px;font-weight:700}
.role{top:184px;width:100%;font-size:9px;color:var(--soft)}
.dots{top:212px;left:590px;display:flex;gap:5px}
.dots i{width:6px;height:6px;border-radius:50%;background:#fff;display:block}

/* contact */
.contact{top:1985px;height:272px;background:linear-gradient(180deg,var(--blue) 0%,var(--blue-deep) 100%)}
.contact .section-title{position:absolute;right:629px;top:46px;font-size:20px}
.contact-text{right:629px;top:90px;width:220px;text-align:right;font-size:9px;line-height:14px}
.socials{left:506px;top:166px;display:flex;gap:8px}
.socials span{width:15px;height:15px;border-radius:50%;background:#b8c6d4;display:block}
.contact-form{left:640px;top:50px;width:282px}
.field{display:block;width:282px;height:32px;border:1px solid var(--line);margin-bottom:7px}
.field.message{height:62px}
.send{width:282px;height:30px;background:var(--night);border:0;color:#fff;font:9px 'Lato',sans-serif;text-transform:uppercase;letter-spacing:.5px}

footer{top:2257px;height:46px;background:var(--black);text-align:center;font-size:8px;line-height:46px;color:#666}
</style>
</head>
<body>

<header class="hero">
  <div class="hero-art" role="img" aria-label="Dark hexagonal mesh backdrop with soft light rays behind the brand badge"></div>
  <div class="brand-badge">HALDEN GROUP</div>
  <h1 class="tagline">INTELLIGENCE BASED DUE DILIGENCE</h1>
</header>

<nav class="main-nav">
  <span class="abs nav-brand">HALDEN</span>
  <ul class="abs nav-links">
    <li>Home</li><li>About Us</li><li>Services</li><li>Clients</li><li>Contact</li>
  </ul>
</nav>

<section class="about">
  <h2 class="section-title">ABOUT US</h2>
  <p>We help small technology, engineering and unmanned systems firms enter the defence market. Our analysts map agency needs, vet partners and build a clear route to contract for teams with strong products and little time.</p>
  <span class="text-link">meet our team</span>
</section>

<section class="what" role="img" aria-label="Business team meeting around a table, tinted blue">
  <h2 class="abs what-title">What is<br>Halden Group</h2>
  <p class="abs what-lead">A growing team of innovative, tenacious thinkers who thrive on solving complicated problems for firms selling to defence buyers.<br><br>We study each market, test every claim and shape the plan that moves a product from idea to award with less delay.</p>
  <span class="abs text-link what-more">read more about our company</span>
  <div class="abs what-side">
    <h3>Simple dummy text</h3>
    <p>Focused acceleration for young companies with sound ideas and a clear need for federal buyers.<br><br>We open the right doors and keep the path to market short.</p>
  </div>
</section>

<section class="services">
  <h2 class="section-title">OUR SERVICES</h2>
  <p class="abs services-intro">From first research to final bid, we guide teams through each step of selling to military and intelligence agencies, so growth comes sooner and costs stay low.</p>
  <div class="abs services-art" role="img" aria-label="Illustration of a glowing light bulb with a pencil and small grey circles"></div>
  <div class="abs we-serve">WE SERVE</div>

  <div class="abs service" style="left:583px;top:211px">
    <svg width="18" height="18" viewBox="0 0 18 18" fill="#ccc"><circle cx="9" cy="9" r="3"/><circle cx="2" cy="2" r="2"/><circle cx="16" cy="2" r="2"/><circle cx="2" cy="16" r="2"/><circle cx="16" cy="16" r="2"/><path d="M2 2L16 16M16 2L2 16" stroke="#ccc"/></svg>
    <h4>Lorem ipsum simple</h4>
    <p>Market mapping that shows which agencies need your product today.</p>
  </div>
  <div class="abs service" style="left:818px;top:211px">
    <svg width="20" height="18" viewBox="0 0 20 18" fill="none" stroke="#ccc" stroke-width="1.6"><rect x="1" y="1" width="18" height="12"/><path d="M7 17h6M10 13v4"/></svg>
    <h4>Lorem ipsum simple</h4>
    <p>Technical review of your system against current defence standards.</p>
  </div>
  <div class="abs service" style="left:583px;top:322px">
    <svg width="18" height="18" viewBox="0 0 18 18" fill="none" stroke="#ccc" stroke-width="1.8"><circle cx="7" cy="7" r="5"/><path d="M11 11l6 6"/></svg>
    <h4>Lorem ipsum simple</h4>
    <p>Due diligence on partners, rivals and prime contractors in your field.</p>
  </div>
  <div class="abs service" style="left:818px;top:322px">
    <svg width="20" height="18" viewBox="0 0 20 18" fill="#ccc"><rect x="1" y="11" width="3" height="6"/><rect x="6" y="8" width="3" height="9"/><rect x="11" y="5" width="3" height="12"/><rect x="16" y="1" width="3" height="16"/></svg>
    <h4>Lorem ipsum simple</h4>
    <p>Capture planning that speeds your time to market and first award.</p>
  </div>
</section>

<section class="partners" aria-label="Client marks">
  <span class="partner-mark"></span><span class="partner-mark"></span><span class="partner-mark"></span>
  <span class="partner-mark"></span><span class="partner-mark"></span><span class="partner-mark"></span>
</section>

<section class="testimonial" role="img" aria-label="Empty conference room in grey tones">
  <div class="abs quote-mark">&ldquo;</div>
  <p>Their team found the right buyers for our sensor line within weeks. The guidance was sharp, honest and practical, and it cut our path to a first contract by half a year.</p>
  <div class="abs author">DANA WHITFIELD</div>
  <div class="abs role">Meridian CEO</div>
  <div class="abs dots"><i></i><i></i><i></i></div>
</section>

<section class="contact">
  <h2 class="section-title">GET IN TOUCH</h2>
  <p class="abs contact-text">Do you have a potential project you'd like to discuss or simply want to get in touch? Send us an e-mail at info@example.com or use the contact form on the right.</p>
  <div class="abs socials"><span></span><span></span><span></span></div>
  <form class="abs contact-form">
    <span class="field"></span>
    <span class="field"></span>
    <span class="field message"></span>
    <button class="send" type="button">Send Message</button>
  </form>
</section>

<footer>Copyright 2015 Halden Group. All rights reserved.</footer>
</body>
</html>
```